KORVELTA Corporate Business Card

Modern business card design for company which focuses in the areas of Staffing, IT Consulting & Data Services. Please note: We are no longer using the IT subscript on the logo. All designs should have IT subscript removed.
Website: www.korveltait.example

```html
<!DOCTYPE html>
<html lang="en">
<head>
<meta charset="utf-8">
<title>KORVELTA Business Card</title>
<link rel="stylesheet" href="https://fonts.googleapis.com/css2?family=Arimo:ital,wght@0,400;0,700;1,400&display=swap">
<style>
  :root {
    --brand-blue: #0b5d9c;
    --bright-blue: #1a93d8;
    --ink: #3f4246;
    --paper: #f7f8f9;
    --backdrop: #e4e6e9;
  }
  * { margin: 0; padding: 0; box-sizing: border-box; }
  html, body { width: 1200px; height: 864px; overflow: hidden; }
  body {
    background: var(--backdrop);
    font-family: "Arimo", Arial, sans-serif;
    display: flex;
    flex-direction: column;
    align-items: center;
    justify-content: center;
    gap: 40px;
  }
  .card {
    width: 665px;
    height: 380px;
    position: relative;
    box-shadow: 0 8px 24px rgba(0,0,0,0.18);
  }
  /* front */
  .card-front { background: var(--paper); color: var(--ink); }
  .brand {
    position: absolute; left: 44px; top: 38px;
    display: flex; align-items: center; gap: 14px;
  }
  .brand-mark {
    width: 40px; height: 40px; background: var(--brand-blue);
  }
  .brand-name {
    font-weight: 700; font-size: 54px; letter-spacing: 3px;
    color: var(--bright-blue); line-height: 1;
  }
  .person { position: absolute; left: 44px; top: 128px; }
  .person-name { font-size: 28px; letter-spacing: 1px; color: var(--ink); }
  .person-role { font-size: 20px; font-style: italic; color: var(--bright-blue); margin-top: 4px; }
  .divider { position: absolute; left: 44px; top: 200px; width: 570px; height: 6px; }
  .divider-strong { position: absolute; left: 0; top: 0; width: 190px; height: 6px; background: var(--brand-blue); }
  .divider-thin { position: absolute; left: 190px; top: 4px; right: 0; height: 2px; background: var(--bright-blue); }
  .contact { position: absolute; font-size: 17px; color: var(--ink); display: flex; align-items: center; gap: 10px; }
  .contact svg { width: 20px; height: 20px; flex: none; }
  .contact-phone { left: 44px; top: 222px; }
  .contact-email { left: 262px; top: 222px; }
  .contact-address { left: 44px; top: 262px; }
  .contact-web { left: 44px; top: 300px; font-weight: 700; color: var(--brand-blue); }
  .corner-decor {
    position: absolute; right: 28px; bottom: 24px; width: 140px; height: 110px;
    background: linear-gradient(135deg, rgba(200,204,210,0) 0%, rgba(200,204,210,0.55) 100%);
  }
  /* back */
  .card-back {
    background: var(--brand-blue);
    display: flex; align-items: center; justify-content: center;
  }
  .card-back .brand { position: static; }
  .card-back .brand-mark { width: 58px; height: 58px; background: #ffffff; }
  .card-back .brand-name { color: #ffffff; font-size: 78px; }
</style>
</head>
<body>
  <section class="card card-front">
    <div class="brand">
      <span class="brand-mark"></span>
      <span class="brand-name">KORVELTA</span>
    </div>
    <div class="person">
      <p class="person-name">DANIEL REYES</p>
      <p class="person-role">General Manager</p>
    </div>
    <div class="divider">
      <span class="divider-strong"></span>
      <span class="divider-thin"></span>
    </div>
    <p class="contact contact-phone">
      <svg viewBox="0 0 20 20" aria-hidden="true"><rect width="20" height="20" rx="3" fill="#0b5d9c"/><rect x="6" y="4" width="8" height="12" rx="1.5" fill="none" stroke="#fff" stroke-width="1.6"/></svg>
      555-014-2790
    </p>
    <p class="contact contact-email">
      <svg viewBox="0 0 20 20" aria-hidden="true"><rect width="20" height="20" rx="3" fill="#0b5d9c"/><rect x="4" y="6" width="12" height="8" fill="none" stroke="#fff" stroke-width="1.5"/><path d="M4 6l6 5 6-5" fill="none" stroke="#fff" stroke-width="1.5"/></svg>
      contactus@korveltait.example
    </p>
    <p class="contact contact-address">418 Larkin St. Ashford, IN 47000</p>
    <p class="contact contact-web">www.korveltait.example</p>
    <div class="corner-decor" role="img" aria-label="Faint decorative cluster of scattered squares"></div>
  </section>

  <section class="card card-back">
    <div class="brand">
      <span class="brand-mark"></span>
      <span class="brand-name">KORVELTA</span>
    </div>
  </section>
</body>
</html>
```